Technical product manual needs upgrade

For a US-based company called TRV Fasteners, Inc (www.trv-fasteners.example) we need to make our product manual more attractive. The product described in the manual is a metal clamp used for mounting cylinder-shaped industrial parts. All the information is already there, but it misses attractiveness, lacks company identity and perhaps the information should be rearranged to make it easier to understand. The print would be on one-sided A3 size paper. The final design should incorporate our company colors / logo / identity (though not too much) and communicate a sense of industrial reliability and attention for detail. However, the design should be easy to understand and not distract from the end goal of being a product manual.

Target Market(s)

Installation engineers / service engineers / purchasers

Industry/Entity Type

It Company

Font styles to use
Serif
Sans Serif

Colors

Designer to choose colors to be used in the design.

Requirements
Must have
• Easy to understand structure / arrangement of information
• Professional / reliable look
• Company colors but not too much since it is a manual that will be printed
• #1abc9c
• #193441
• Company logo
Nice to have
• #ecab18
Should not have
• A backside (project is one-sided paper)
• Should not be 'over the top'

```html
<!DOCTYPE html>
<html lang="en">
<head>
<meta charset="utf-8">
<title>TRV Fasteners – Parts List, Recommendations, Instructions</title>
<link href="https://fonts.googleapis.com/css2?family=Source+Sans+3:ital,wght@0,400;0,600;0,700;0,800;1,700&display=swap" rel="stylesheet">
<style>
:root{
  --amber:#ecab18;
  --slate:#5d7c93;
  --slate-dark:#4a6a82;
  --navy:#193441;
  --teal:#1abc9c;
  --cream:#fdf4e3;
  --line:#9aa;
  --art:#dfe3e6;
}
*{box-sizing:border-box;margin:0;padding:0}
html,body{width:848px;height:1200px;overflow:hidden;background:#fff}
body{font-family:"Source Sans 3",Arial,sans-serif;color:var(--navy);position:relative}
.abs{position:absolute}
.band-top{left:0;top:0;width:848px;height:18px;background:var(--amber)}
.brand{left:0;top:46px;width:848px;text-align:center;font-size:50px;font-weight:800;color:var(--slate);letter-spacing:1px;line-height:60px}
.brand .dot{display:inline-block;width:30px;height:30px;border-radius:50%;background:var(--teal);margin-right:14px;vertical-align:middle}
.page-title{left:34px;top:122px;font-size:40px;font-weight:700;color:var(--slate);white-space:nowrap;line-height:48px}
.page-title .sep{font-weight:400;color:#9bb0c0;margin:0 6px}
.section-bar{height:28px;background:linear-gradient(90deg,var(--slate) 0%,var(--slate) 35%,rgba(93,124,147,0) 100%);color:#fff;font-weight:700;font-size:23px;padding-left:32px;line-height:28px}
.section-bar small{font-size:16px;margin-left:50px}
.parts-table{left:32px;top:207px;width:360px;border-collapse:collapse;font-size:15px}
.parts-table th{background:var(--amber);color:#fff;font-size:13px;font-weight:700;height:22px}
.parts-table td{border:1px solid var(--line);vertical-align:top;padding:2px 8px;line-height:17px;height:38px}
.parts-table td:nth-child(1),.parts-table td:nth-child(2){text-align:center;width:34px}
.parts-art{left:400px;top:212px;width:245px;height:206px;background:var(--art);border-radius:4px}
.side-head{left:652px;width:190px;background:var(--amber);color:#fff;font-weight:700;font-size:19px;line-height:17px;padding:3px 10px}
.side-list{left:660px;font-size:15px;line-height:19px;list-style:none}
.side-list li::before{content:"• "}
.notice{left:0;top:425px;width:848px;height:65px;background:var(--amber);text-align:center}
.notice h2{font-size:24px;font-weight:800;line-height:30px;margin-top:3px}
.notice p{font-size:14px;line-height:16px;padding:0 30px}
.cream{left:0;top:490px;width:848px;height:538px;background:var(--cream)}
.sub{left:0;width:848px;height:20px}
.sub::before{content:"";position:absolute;left:0;top:2px;width:26px;height:16px;background:var(--amber)}
.sub h3{position:absolute;left:32px;top:-2px;font-size:18px;font-weight:700;color:var(--slate);white-space:nowrap}
.sub h3 em{font-size:13px;font-weight:700}
.body-text{font-size:13.5px;font-weight:700;line-height:17px}
.body-text ol{padding-left:0;list-style:none}
.body-text li{padding-left:14px;text-indent:-14px}
.steps-art{left:455px;top:648px;width:360px;height:352px;background:linear-gradient(180deg,var(--cream),#ebe3d3);border-radius:4px}
.footer-brand{left:32px;top:1040px;font-size:28px;font-weight:800;color:var(--slate)}
.footer-brand .dot{display:inline-block;width:18px;height:18px;border-radius:50%;background:var(--teal);margin-right:8px;vertical-align:middle}
.contact{left:236px;top:1042px;width:576px;text-align:center;white-space:nowrap}
.contact strong{display:block;font-size:22px;color:var(--slate-dark);font-weight:700;line-height:26px}
.contact span{font-size:14.5px;font-weight:700}
.disclaimer{left:0;top:1098px;width:848px;height:102px;background:var(--amber);font-size:14px;font-weight:700;text-align:center;padding:12px 30px;line-height:17px}
</style>
</head>
<body>
<div class="abs band-top"></div>
<div class="abs brand"><span class="dot"></span>TRV Fasteners</div>
<h1 class="abs page-title">Parts List<span class="sep">|</span>Recommendations<span class="sep">|</span>Instructions</h1>

<div class="abs section-bar" style="left:0;top:172px;width:848px">PARTS LIST<small>(1Clamp)</small></div>

<table class="abs parts-table">
<tr><th>Item</th><th>Qty</th><th>Description</th><th>Meterial</th></tr>
<tr><td>1</td><td>1</td><td>Clamp body<br>single bolt</td><td>Steel Zn<br>&nbsp;plated</td></tr>
<tr><td>2</td><td>1</td><td>Hex cap screw<br>7/16x3.25</td><td>Zinc plated,<br>&nbsp;steel, mild</td></tr>
<tr><td>3</td><td>1</td><td>Hex nuts 7/16</td><td>Zinc plated,<br>&nbsp;steel, mild</td></tr>
<tr><td>4</td><td>2</td><td>Upper protection<br>rubber</td><td>EPDM rubbershore<br>&nbsp;hardness65°±5°</td></tr>
<tr><td>5</td><td>2</td><td>Lower protection<br>rubber</td><td>EPDM rubbershore<br>&nbsp;hardness65</td></tr>
</table>

<div class="abs parts-art" role="img" aria-label="Exploded drawing of the clamp parts numbered 1 to 5"></div>

<div class="abs side-head" style="top:207px">Required<br>tooling</div>
<ul class="abs side-list" style="top:254px"><li>Spanner</li><li>Torque wrench</li><li>Level tool</li></ul>
<div class="abs side-head" style="top:316px">Recommended<br>protection<br>measures</div>
<ul class="abs side-list" style="top:380px"><li>Safety gloves</li><li>Safety goggles</li></ul>

<div class="abs notice">
<h2>Accumulator assembly recommendations</h2>
<p>For the positioning and assembly of any hydraulic accumulator above 50 Lbs. we advise to always use an accumulator lifting cap. Please refer to your accumulator supplier for this.</p>
</div>

<div class="abs cream"></div>
<div class="abs section-bar" style="left:0;top:501px;width:848px;font-size:25px">Instructions</div>

<div class="abs sub" style="top:538px"><h3>Assembly of rubber onto clamp (<em>We advise you to use safety gloves for the assembly of the clamp)</em></h3></div>
<div class="abs body-text" style="left:82px;top:557px;width:660px"><ol>
<li>1. Place lower protection rubbers (item no. 5) on to the inside of the lower clamp half and fold edges of the rubber over the clamp band, as shown in images A, B, C and D.</li>
<li>2. Place upper protection rubbers (item no. 4) on to the inside of the upper clamp half and fold edges of the rubber over the clamp band, as shown in images E, F, G and H.</li>
</ol></div>

<div class="abs sub" style="top:630px"><h3>Mounting of clamp onto wall / frame / etc.</h3></div>
<div class="abs body-text" style="left:68px;top:650px;width:378px">We recommend you to mount your clamp onto a stable surface and to always use a levelling tool. The mounting materials used should be in accordance with the mounting holes already present on the clamp. The mounting holes are located on the bottom of the mounting part of the clamp and are NOT the same holes as the holes for the hex cap screw.</div>

<div class="abs sub" style="top:757px"><h3>Positioning of accumulator</h3></div>
<div class="abs body-text" style="left:68px;top:777px;width:360px">Position your accumulator into the open clamp(s) as described by your accumulator supplier.</div>

<div class="abs sub" style="top:816px"><h3>Tightening hex cap screw and closing clamp</h3></div>
<div class="abs body-text" style="left:60px;top:835px;width:392px">Adjust your torque wrench to the advised torque level of 35nm
<ol style="margin-left:22px;margin-top:1px">
<li>1. Place the hex cap screw (item no. 2) fully through the bolt holes until the cap (head) of the screw touches the spacer, as &nbsp;shown in images I and J.</li>
<li>2. Place the hex nut (item no. 3) on the end of the hex cap screw, as shown in imagesK and L.</li>
<li>3. Place the spanner on the bolt head.</li>
<li>4. Place the torque wrench on the hex nut.</li>
<li>5. Hold the spanner steady and use the torque wrench to reach the advised torque level.</li>
<li>6. Check if accumulator is mounted securely.</li>
</ol></div>

<div class="abs steps-art" role="img" aria-label="Step drawings A to L showing rubber placement and screw tightening on the clamp"></div>

<div class="abs footer-brand"><span class="dot"></span>TRV Fasteners</div>
<div class="abs contact"><strong>TRV Fasteners, Inc.</strong><span>1420 Harbor Loop Suite 200 Dayton, TX 77535 E: info@trv-fasteners.example T: 1-555-014-2290</span></div>

<div class="abs disclaimer">The sole purpose of this product manual is to provide instructions for mounting the accumulator clamps as supplied by TRV Fasteners, Inc. Please keep in mind that TRV Fasteners, Inc. manufactures nor sells accumulators and is in no way liable for any damage or injury involving the handling, moving or mounting of accumulators itself.</div>
</body>
</html>
```